Need Eye Catching For Sale By Owner Signs

In need of a Eye Catching For Sale By Owner Sign design. I plan on using the sign to market buildings and raw land that I own. The design should be able to scale to different rectangular dimensions for example a yard stake sign or a large 4' x 6' sign to be tacked to plywood. The design should have a dead space near the bottom that I can insert more detail information into at a later time.

The main tag line "For Sale By Owner" and the contact number "318-562-4097" needs to be easily be read from a distance.

```html
<!DOCTYPE html>
<html lang="en">
<head>
<meta charset="utf-8">
<title>For Sale By Owner Sign</title>
<link rel="stylesheet" href="https://fonts.googleapis.com/css2?family=Anton&family=Archivo+Black&family=Open+Sans:wght@500&display=swap">
<style>
  :root {
    --sign-blue: #0a93e8;
    --sign-red: #ff0000;
    --paper: #ffffff;
    --mug-glass: #f3f6e8;
    --mug-beer: #f8f4b0;
  }
  html, body {
    margin: 0;
    padding: 0;
    width: 921px;
    height: 1200px;
    overflow: hidden;
    background: var(--paper);
  }
  .sign {
    position: relative;
    width: 921px;
    height: 1200px;
    background: var(--paper);
  }
  .headline-free {
    position: absolute;
    left: 0;
    top: 0;
    width: 921px;
    height: 600px;
  }
  .headline-free text {
    font-family: "Anton", "Impact", sans-serif;
    fill: var(--sign-blue);
  }
  .mug-tile {
    position: absolute;
    left: 424px;
    top: 199px;
    width: 432px;
    height: 415px;
    border-radius: 34px;
    background: radial-gradient(ellipse at 45% 50%, var(--mug-beer) 0%, var(--mug-glass) 32%, var(--sign-red) 33%);
  }
  .joke-note {
    position: absolute;
    left: 28px;
    top: 556px;
    margin: 0;
    font-family: "Open Sans", "Verdana", sans-serif;
    font-weight: 500;
    font-size: 50px;
    line-height: 1;
    color: var(--sign-blue);
  }
  .sale-info {
    position: absolute;
    left: 0;
    width: 864px;
    margin: 0;
    text-align: center;
    font-family: "Archivo Black", "Arial Black", sans-serif;
    color: var(--sign-red);
    line-height: 1;
  }
  .sale-tagline { top: 634px; font-size: 47px; letter-spacing: 2px; }
  .sale-call { top: 698px; font-size: 44px; letter-spacing: 2px; }
  .sale-phone { top: 762px; font-size: 47px; letter-spacing: 2px; }
</style>
</head>
<body>
  <main class="sign">
    <svg class="headline-free" viewBox="0 0 921 600" aria-label="Free, with asterisk">
      <text x="25" y="557" font-size="496" textLength="385" lengthAdjust="spacingAndGlyphs">FREE</text>
      <text x="868" y="268" font-size="110">*</text>
    </svg>
    <div class="mug-tile" role="img" aria-label="Tilted mug of foamy beer on a red rounded square"></div>
    <p class="joke-note">*Just kidding</p>
    <p class="sale-info sale-tagline">FOR SALE BY OWNER</p>
    <p class="sale-info sale-call">CALL</p>
    <p class="sale-info sale-phone">318-562-4097</p>
  </main>
</body>
</html>
```